Business Bench-marking brochure

Create a single page flyer for an account firm to advertise their Business Bench-marking product offering.

Style should follow new corporate image in development as per attached website psd.

The client likes the logo to always be on the RIGHT of publications.

Target Market(s)

Small - Medium sucessfully Business

Industry/Entity Type

Business

Colors
eb1f27

Requirements
Nice to have
• The client would like an image of a scales with Apples on both sides to be used -the idea being "comparing apples to apples"

```html
<!DOCTYPE html>
<html lang="en">
<head>
<meta charset="utf-8">
<title>How Does Your Business Compare? – Fenwick Business Consulting</title>
<link rel="stylesheet" href="https://fonts.googleapis.com/css2?family=Roboto:wght@300;400;500;700;900&display=swap">
<style>
  :root {
    --brand-red: #eb1f27;
    --deep-red: #98222a;
    --ink: #111111;
    --paper: #ffffff;
    --photo-light: #f4f4f4;
    --photo-mid: #d9d9d9;
  }
  * { box-sizing: border-box; margin: 0; padding: 0; }
  html, body { width: 927px; height: 1200px; overflow: hidden; background: var(--paper); }
  body { font-family: 'Roboto', Arial, sans-serif; color: var(--ink); }

  .flyer { position: relative; width: 927px; height: 1200px; overflow: hidden; background: var(--paper); }

  .site-url {
    position: absolute; top: 28px; right: 40px;
    font-weight: 700; font-size: 16px; color: var(--deep-red); letter-spacing: 0.2px;
  }

  .headline {
    position: absolute; top: 88px; left: 74px;
    font-weight: 300; font-size: 63px; line-height: 60px; letter-spacing: 0.5px; color: var(--ink);
  }
  .headline strong { font-weight: 900; }

  .hero-image {
    position: absolute; top: 228px; left: 90px; width: 760px; height: 446px;
    background: radial-gradient(ellipse at 50% 60%, var(--photo-mid) 0%, var(--photo-light) 55%, var(--paper) 80%);
  }

  .offer-panel { position: absolute; top: 672px; left: 0; width: 927px; height: 440px; }
  .offer-panel svg { position: absolute; inset: 0; }

  .intro { position: absolute; top: 718px; left: 55px; width: 278px; color: var(--paper); }
  .intro h2 { font-weight: 700; font-size: 15.5px; line-height: 19px; margin-bottom: 19px; }
  .intro p { font-weight: 300; font-size: 16px; line-height: 19.5px; }

  .benefits { position: absolute; top: 722px; left: 373px; width: 530px; color: var(--paper); }
  .benefits h3 { font-weight: 700; font-size: 15.5px; margin-bottom: 14px; }
  .benefit-list { list-style: none; }
  .benefit-list li {
    display: flex; align-items: center; gap: 6px;
    font-weight: 500; font-size: 16px; line-height: 19px; margin-bottom: 14px;
  }
  .benefit-list svg { flex: none; }
  .cta { width: 500px; margin-top: 34px; font-weight: 300; font-size: 15.5px; line-height: 18px; }
  .cta p { margin-bottom: 10px; }

  .contact { position: absolute; left: 55px; top: 1122px; }
  .contact-row { display: flex; align-items: center; gap: 9px; }
  .contact-phone { font-size: 25px; font-weight: 400; color: var(--ink); }
  .contact-email { margin-top: 10px; font-size: 16px; font-weight: 500; color: var(--ink); }

  .brand {
    position: absolute; right: 42px; top: 1128px;
    display: flex; align-items: center; gap: 10px;
    font-weight: 500; font-size: 22px; color: var(--ink);
  }
  .brand-mark { width: 14px; height: 14px; background: var(--brand-red); }
</style>
</head>
<body>
<main class="flyer">
  <div class="site-url">www.fenwickadvisory.com.au</div>

  <h1 class="headline">HOW DOES YOUR<br>BUSINESS <strong>COMPARE</strong>?</h1>

  <div class="hero-image" role="img" aria-label="A balance scale weighing a green apple against a red apple"></div>

  <section class="offer-panel">
    <svg width="927" height="440" viewBox="0 0 927 440" aria-hidden="true">
      <path d="M0 0 H927 V372 C760 372 560 370 460 374 C400 377 380 420 320 432 L0 432 Z" fill="var(--deep-red)"/>
      <path d="M0 432 L320 432 C380 420 400 377 460 374 C560 370 760 372 927 372 V392 C760 390 560 390 470 393 C410 396 390 436 330 440 L0 440 Z" fill="var(--brand-red)"/>
    </svg>
  </section>

  <div class="intro">
    <h2>Ever wondered how your business compares to your competitors?</h2>
    <h2>Why you may be struggling to make a profit while other businesses in your industry seem to have it all figured out?</h2>
    <p>By capturing the financial information and KPIs of your business we can compare your business to those within your industry. This enables you to be armed with the knowledge of how you can take corrective action by making informed decisions to save money and significantly enhance your overall performance</p>
  </div>

  <div class="benefits">
    <h3>Benchmarking helps you:</h3>
    <ul class="benefit-list">
      <li><svg width="18" height="14" viewBox="0 0 18 14"><path d="M2 1 L8 7 L2 13 M8 1 L14 7 L8 13" fill="none" stroke="#fff" stroke-width="1.4"/></svg>Identify where you can reduce costs and improve efficiencies</li>
      <li><svg width="18" height="14" viewBox="0 0 18 14"><path d="M2 1 L8 7 L2 13 M8 1 L14 7 L8 13" fill="none" stroke="#fff" stroke-width="1.4"/></svg>Determine the productivity of your employees</li>
      <li><svg width="18" height="14" viewBox="0 0 18 14"><path d="M2 1 L8 7 L2 13 M8 1 L14 7 L8 13" fill="none" stroke="#fff" stroke-width="1.4"/></svg>Highlight opportunities for improvement and innovative practices</li>
      <li><svg width="18" height="14" viewBox="0 0 18 14"><path d="M2 1 L8 7 L2 13 M8 1 L14 7 L8 13" fill="none" stroke="#fff" stroke-width="1.4"/></svg>Discover opportunities for making your business more competitive</li>
    </ul>
    <div class="cta">
      <p>To ensure your business is operating at its peak performance, call Fenwick Business Consulting for your detailed benchmark report.</p>
      <p>Full analysis of your financial statements, including KPIs, along with a meeting with Claire Fenwick to identify areas to improve to help your business prosper.</p>
    </div>
  </div>

  <div class="contact">
    <div class="contact-row contact-phone">
      <svg width="20" height="20" viewBox="0 0 20 20" aria-hidden="true"><circle cx="10" cy="10" r="8.5" fill="none" stroke="var(--brand-red)" stroke-width="1.6"/><path d="M7 5.5 C5.5 7 6 10 8 12 C10 14 13 14.5 14.5 13 L12.8 11.2 L11.3 12 C10 11.4 8.6 10 8 8.7 L8.8 7.2 Z" fill="var(--brand-red)"/></svg>
      <span>02 4000 1234</span>
    </div>
    <div class="contact-row contact-email">
      <svg width="20" height="14" viewBox="0 0 20 14" aria-hidden="true"><rect x="0.5" y="0.5" width="19" height="13" fill="var(--brand-red)"/><path d="M1 1 L10 8 L19 1" fill="none" stroke="#fff" stroke-width="1.4"/></svg>
      <span>admin@fenwickadvisory.com.au</span>
    </div>
  </div>

  <div class="brand">
    <span class="brand-mark" aria-hidden="true"></span>
    <span class="brand-name">Fenwick Business Consulting</span>
  </div>
</main>
</body>
</html>
```